K&T Holdings

Design a modern simple business card. I have attached a clean version of a card we like form Marrowfield Partners another company we own. I also attached the old K&T card design and logo and a couple of ideas we had but just can't finalize on whether we like them or not. We would like to include the 20 year logo somewhere on the card.

```html
<!DOCTYPE html>
<html lang="en">
<head>
<meta charset="utf-8">
<title>K&amp;T Holdings – Business Card</title>
<link href="https://fonts.googleapis.com/css2?family=Montserrat:wght@400;500;700&display=swap" rel="stylesheet">
<style>
  :root {
    --navy: #1c1d4f;
    --grey: #6d6d70;
    --rule: #3a3b6b;
    --paper: #ffffff;
    --backdrop: #d4d6d7;
    --mark-fill: #e4e5ec;
  }
  * { box-sizing: border-box; margin: 0; padding: 0; }
  html, body { width: 1200px; height: 829px; overflow: hidden; }
  body {
    background: var(--backdrop);
    font-family: "Montserrat", sans-serif;
    display: flex;
    align-items: center;
    justify-content: center;
    gap: 60px;
  }
  .card {
    position: relative;
    width: 520px;
    height: 297px;
    background: var(--paper);
    box-shadow: 0 6px 18px rgba(0,0,0,.12);
    border-bottom: 4px solid var(--navy);
  }
  .brand {
    display: flex;
    align-items: center;
    gap: 8px;
    color: var(--navy);
    font-weight: 700;
    font-size: 34px;
    letter-spacing: 1px;
  }
  .brand-dot {
    width: 12px; height: 12px;
    border-radius: 50%;
    background: var(--navy);
  }

  /* Front */
  .card-front .brand { position: absolute; top: 48px; left: 232px; }
  .front-info {
    position: absolute;
    top: 128px; left: 0; right: 0;
    display: flex;
    justify-content: center;
  }
  .person { text-align: right; padding-right: 16px; padding-top: 4px; }
  .person-name { color: var(--navy); font-weight: 700; font-size: 20px; letter-spacing: .5px; }
  .person-title { color: var(--grey); font-size: 12px; margin-top: 2px; }
  .divider-v { width: 1px; background: var(--rule); }
  .contacts { list-style: none; padding-left: 14px; }
  .contacts li {
    display: flex; align-items: center; gap: 6px;
    color: var(--grey); font-size: 12.5px; line-height: 19px;
  }
  .contacts svg { width: 10px; height: 10px; fill: var(--navy); flex: none; }
  .office {
    position: absolute; bottom: 30px; left: 0; right: 0;
    text-align: center;
  }
  .office-label { color: var(--navy); font-weight: 700; font-size: 12.5px; }
  .office-address { color: var(--grey); font-size: 13px; margin-top: 2px; }

  /* Back */
  .back-top {
    position: absolute; top: 62px; left: 0; right: 0;
    display: flex; justify-content: center; align-items: center; gap: 28px;
  }
  .card-back .brand { font-size: 44px; }
  .back-top .divider-v { height: 120px; }
  .anniversary-mark {
    width: 150px; height: 100px;
    background: linear-gradient(135deg, var(--mark-fill), #d6d7e2);
    border-radius: 4px;
  }
  .services {
    position: absolute; bottom: 34px; left: 0; right: 0; text-align: center;
  }
  .services-title { color: var(--navy); font-weight: 700; font-size: 13px; }
  .services-list { color: var(--grey); font-size: 12px; margin-top: 3px; }
</style>
</head>
<body>

  <section class="card card-front">
    <div class="brand"><span class="brand-dot"></span>K&amp;T</div>
    <div class="front-info">
      <div class="person">
        <div class="person-name">DANIEL WHITFORD</div>
        <div class="person-title">President and Coo</div>
      </div>
      <div class="divider-v"></div>
      <ul class="contacts">
        <li><svg viewBox="0 0 10 10"><rect x="2.5" y="0" width="5" height="10" rx="1"/></svg>713-555-0142</li>
        <li><svg viewBox="0 0 10 10"><path d="M0 4q5-4 10 0v2H7V4.5H3V6H0z"/><rect x="1.5" y="6.5" width="7" height="3.5" rx=".5"/></svg>877-555-0199</li>
        <li><svg viewBox="0 0 10 10"><path d="M0 2h10v6H0z M0 2l5 3.5L10 2" /></svg>Daniel@marrowfieldpartners.com</li>
        <li><svg viewBox="0 0 10 10"><circle cx="5" cy="5" r="5"/></svg>www.marrowfieldpartners.com</li>
      </ul>
    </div>
    <div class="office">
      <div class="office-label">Corporate:</div>
      <div class="office-address">1180 Harbor Avenue, Suite 410, Port Calder, TX 77790</div>
    </div>
  </section>

  <section class="card card-back">
    <div class="back-top">
      <div class="brand"><span class="brand-dot"></span>K&amp;T</div>
      <div class="divider-v"></div>
      <div class="anniversary-mark" role="img" aria-label="20-year anniversary mark, 2004 to 2024"></div>
    </div>
    <div class="services">
      <div class="services-title">Integrated Industrial Services</div>
      <div class="services-list">Mechanical/Civil I&amp;E Fabrication Rotating Heat Transfer Equipment</div>
    </div>
  </section>

</body>
</html>
```